Asphalt Paving Specialists Business Cards

Our company is TREVIN ASPHALT. We need a business cards two of our asphalt paving team members. We're asphalt specialists.
I need two made up please. The details on the front of the each business card i would like please is as follows.
Address is 87 Marrowby St, Clontarf, QLD, 4019.

Company Director
Gordon Pelliway
gord@trevinpave.com.au
04 58 736 042
www.trevinpave.com.au

Supervisor
Curtis Vonnegard
curtis@trevinpave.com.au
0462 873 105
www.trevinpave.com.au

We do all aspects of Asphalt Paving. Specific Services include - Driveways, Carparks & sub-divisions. All Roads. Repairs and Maintenance.

We provide free quotes!

I dont have a certain way i want them to look so im open to all designs :)

** I have uploaded our logo for the TREVIN ASPHALT. HOWEVER, CAN YOU PLEASE GET RID OF THE ( PTY LTD )

Thank you
Renata Fulch
TREVIN ASPHALT

Target Market(s)

Home owners and Business Owners

Contact Information for Business Card

Asphalt Paving Specialists. All aspects of Asphalt. Residential, Commercial & Industrial. Based in Brisbane.

Font styles to use
Sans Serif

Colors

Designer to choose colors to be used in the design.

Requirements
Nice to have
• maybe an image of a driveway? or Asphalt?

```html
<!DOCTYPE html>
<html lang="en">
<head>
<meta charset="utf-8">
<title>Trevin Asphalt Business Cards</title>
<link rel="stylesheet" href="https://fonts.googleapis.com/css2?family=Arimo:wght@400;700&display=swap">
<style>
  :root {
    --stage: #dcdddf;
    --card-light: #bccfee;
    --card-mid: #7cc3e8;
    --card-deep: #45b3e3;
    --back-top: #a6cbec;
    --back-bottom: #10ade2;
    --band: #25262b;
    --accent: #1d9edb;
    --ink: #1f2024;
    --paper: #ffffff;
  }
  * { margin: 0; padding: 0; box-sizing: border-box; }
  html, body { width: 1200px; height: 939px; overflow: hidden; }
  body {
    background: var(--stage);
    font-family: "Arimo", Arial, sans-serif;
    position: relative;
  }
  .card {
    position: absolute;
    width: 705px;
    height: 404px;
    overflow: hidden;
  }
  .card-front {
    left: 107px; top: 41px;
    background: linear-gradient(150deg, var(--card-light) 0%, var(--card-mid) 55%, var(--card-deep) 100%);
  }
  .card-back {
    left: 401px; top: 484px;
    height: 402px;
    background: linear-gradient(180deg, var(--back-top) 0%, #5dbce6 45%, var(--back-bottom) 100%);
  }
  .person-name {
    position: absolute; left: 32px; top: 60px;
    font-size: 22px; font-weight: 700; color: var(--accent);
  }
  .person-role {
    position: absolute; left: 32px; top: 90px;
    font-size: 20px; font-weight: 700; color: var(--ink);
  }
  .contact-list {
    position: absolute; left: 32px; top: 251px;
    list-style: none;
  }
  .contact-list li {
    display: flex; align-items: center;
    height: 25.5px;
    font-size: 18px; color: var(--ink);
  }
  .contact-list svg { width: 14px; height: 14px; margin-right: 6px; flex: none; }
  .brand-name {
    position: absolute;
    display: flex; align-items: center; gap: 10px;
    font-weight: 700; white-space: nowrap;
  }
  .card-front .brand-name {
    left: 362px; top: 262px;
    font-size: 30px; color: var(--ink);
  }
  .card-back .brand-name {
    left: 187px; top: 118px;
    font-size: 34px; color: var(--paper);
  }
  .brand-dot { width: 16px; height: 16px; border-radius: 50%; background: currentColor; }
  .rule {
    position: absolute; left: 0; width: 100%; height: 2px; background: var(--band);
  }
  .band {
    position: absolute; left: 0; width: 100%;
    background: var(--band); color: var(--paper);
    display: flex; align-items: center; justify-content: center;
    font-size: 18px;
  }
  .card-front .rule { top: 347px; }
  .card-front .band { top: 353px; height: 51px; }
  .card-back .rule-top { top: 317px; }
  .card-back .band { top: 322px; height: 35px; }
  .card-back .rule-bottom { top: 360px; }
  .services span + span::before {
    content: ""; display: inline-block;
    width: 7px; height: 7px; border-radius: 50%;
    background: var(--paper); margin: 0 4px 2px 5px; vertical-align: middle;
  }
</style>
</head>
<body>
  <section class="card card-front">
    <h1 class="person-name">Gordon Pelliway</h1>
    <p class="person-role">Company Director</p>
    <ul class="contact-list">
      <li>
        <svg viewBox="0 0 14 14" aria-hidden="true"><path d="M3 1 L5.5 1 L6 4 L4.5 5 Q5.5 8 9 9.5 L10 8 L13 8.5 L13 11 Q12 13 9.5 12.5 Q3 10.5 1.5 4 Q1.5 1.5 3 1 Z" fill="var(--accent)"/></svg>
        04 58 736 042
      </li>
      <li>
        <svg viewBox="0 0 14 14" aria-hidden="true"><rect x="1" y="3" width="12" height="8.5" fill="var(--accent)"/><path d="M1 3 L7 8 L13 3" fill="none" stroke="#fff" stroke-width="1"/></svg>
        gord@trevinpave.com.au
      </li>
      <li>
        <svg viewBox="0 0 14 14" aria-hidden="true"><g fill="none" stroke="var(--accent)" stroke-width="1.1"><circle cx="7" cy="7" r="6"/><ellipse cx="7" cy="7" rx="2.6" ry="6"/><path d="M1 7 H13 M2 4 H12 M2 10 H12"/></g></svg>
        www.trevinpave.com.au
      </li>
    </ul>
    <div class="brand-name"><span class="brand-dot"></span>TREVIN ASPHALT</div>
    <div class="rule"></div>
    <p class="band">87 Marrowby St, Clontarf, QLD, 4019</p>
  </section>

  <section class="card card-back">
    <div class="brand-name"><span class="brand-dot"></span>TREVIN ASPHALT</div>
    <div class="rule rule-top"></div>
    <p class="band services"><span>Driveways</span><span>Carparks &amp; sub-divisions</span><span>All Roads</span><span>Repairs and Maintenance</span></p>
    <div class="rule rule-bottom"></div>
  </section>
</body>
</html>
```